BRAVEN EV

We need a business card design for a new Luxury golf cart Company Braven. We manufacture and sell high end golf carts. We would like to see designs that are high end. I have the logo so really need a nice clean look.

```html
<!DOCTYPE html>
<html lang="en">
<head>
<meta charset="utf-8">
<title>Vorlane EV – Business Card</title>
<link href="https://fonts.googleapis.com/css2?family=Archivo:wght@400;800&display=swap" rel="stylesheet">
<style>
  :root {
    --page-bg: #e6e4e4;
    --card-light-top: #f4eeee;
    --card-light-bottom: #e3d9d9;
    --card-dark: #000000;
    --accent-teal: #029c84;
    --name-teal: #2a9d8a;
    --text-light: #f2f2f2;
    --brand-ink: #111111;
  }
  * { margin: 0; padding: 0; box-sizing: border-box; }
  html, body {
    width: 1200px;
    height: 900px;
    overflow: hidden;
    background: var(--page-bg);
    font-family: "Archivo", Arial, sans-serif;
  }
  .business-card {
    position: absolute;
    left: 100px;
    top: 140px;
    width: 1000px;
    height: 619px;
    overflow: hidden;
    background: linear-gradient(180deg, var(--card-light-top), var(--card-light-bottom));
    box-shadow: 0 10px 30px rgba(0,0,0,0.18);
  }
  .card-wave {
    position: absolute;
    inset: 0;
    width: 100%;
    height: 100%;
  }
  .brand-name {
    position: absolute;
    left: 56px;
    top: 118px;
    font-family: "Archivo", Arial, sans-serif;
    font-weight: 800;
    font-size: 80px;
    line-height: 1;
    letter-spacing: 1px;
    color: var(--brand-ink);
    white-space: nowrap;
  }
  .person {
    position: absolute;
    left: 58px;
    top: 430px;
    color: var(--text-light);
  }
  .person-name {
    font-family: "Archivo", Arial, sans-serif;
    font-weight: 800;
    font-size: 40px;
    line-height: 1;
    color: var(--name-teal);
    letter-spacing: 0.3px;
    white-space: nowrap;
  }
  .person-title {
    margin-top: 6px;
    font-weight: 400;
    font-size: 28px;
    line-height: 1.1;
  }
  .contact-list {
    position: absolute;
    right: 69px;
    top: 362px;
    list-style: none;
    color: var(--text-light);
    font-size: 27px;
    line-height: 37px;
    text-align: right;
  }
  .contact-item {
    display: flex;
    align-items: center;
    justify-content: flex-end;
    gap: 14px;
    white-space: nowrap;
  }
  .contact-icon {
    width: 27px;
    height: 27px;
    flex: none;
  }
  .address {
    position: absolute;
    right: 69px;
    top: 492px;
    color: var(--text-light);
    font-style: normal;
    font-size: 27px;
    line-height: 37px;
    text-align: right;
    white-space: nowrap;
  }
</style>
</head>
<body>
  <section class="business-card">
    <svg class="card-wave" viewBox="0 0 1090 675" preserveAspectRatio="none" aria-hidden="true">
      <path d="M0 340 C150 400 300 392 520 330 S820 245 1090 340 L1090 675 L0 675 Z" fill="var(--accent-teal)"/>
      <path d="M0 385 C150 428 300 420 520 357 S840 262 1090 345 L1090 675 L0 675 Z" fill="var(--card-dark)"/>
    </svg>

    <div class="brand-name">VORLANE</div>

    <div class="person">
      <h1 class="person-name">DANIEL HARTWELL</h1>
      <p class="person-title">Managing Director</p>
    </div>

    <ul class="contact-list">
      <li class="contact-item">
        <span>044-987 654 321</span>
        <svg class="contact-icon" viewBox="0 0 24 24" aria-hidden="true">
          <path d="M6.5 3.5 9 6.5 7.5 9c1.2 2.6 3.3 4.7 6 6l2.5-1.5 3 2.5-1.5 3.2C11 19 5 13 3.3 5.2Z" fill="none" stroke="var(--accent-teal)" stroke-width="2" stroke-linejoin="round"/>
          <path d="M14 4.5a6 6 0 0 1 5.5 5.5M14 8a2.5 2.5 0 0 1 2 2" fill="none" stroke="var(--accent-teal)" stroke-width="1.8" stroke-linecap="round"/>
        </svg>
      </li>
      <li class="contact-item">
        <span>info@vorlane-ev.com</span>
        <svg class="contact-icon" viewBox="0 0 24 24" aria-hidden="true">
          <rect x="1.5" y="5" width="21" height="14" fill="var(--accent-teal)"/>
          <path d="M1.5 5 12 13.5 22.5 5M1.5 19l7.5-7M22.5 19 15 12" fill="none" stroke="var(--card-dark)" stroke-width="1.5"/>
        </svg>
      </li>
      <li class="contact-item">
        <span>www.vorlane-ev.com</span>
        <svg class="contact-icon" viewBox="0 0 24 24" aria-hidden="true">
          <g fill="none" stroke="var(--accent-teal)" stroke-width="1.6">
            <circle cx="12" cy="12" r="10"/>
            <ellipse cx="12" cy="12" rx="4.5" ry="10"/>
            <path d="M2 12h20M4 6.5h16M4 17.5h16M12 2v20"/>
          </g>
        </svg>
      </li>
    </ul>

    <address class="address">
      421, Address line goes<br>
      here 45452,Country Name
    </address>
  </section>
</body>
</html>
```